Test and Tag business card design

We are an appliance test and tag company in Brisbane Australia requiring a business card design.
I don't have a logo.
Card front: Matte black background with white font.
Card back: White background with black font colour
Examples are attached
Minimalist design
Reason: Looking for more designs with an extreme minimal feel
Industry/Entity Type
Appliance
Contact Information for Business Card
Business name: Summit Check and Label
Description: Onsite Electrical Testing and Tagging
Licence No. 48213
Name: Greg Palmby
Mobile: 0417 592 348
Email: greg@summitcheckandlabel.com.au
Web: summitcheckandlabel.com.au
Logo Text
Summit Check and Label
Look and feel

```html
<!DOCTYPE html>
<html lang="en">
<head>
<meta charset="utf-8">
<title>Summit Check and Label — Business Card</title>
<link rel="stylesheet" href="https://fonts.googleapis.com/css2?family=Josefin+Slab:wght@400;600;700&family=Yellowtail&display=swap">
<style>
  :root {
    --matte: #161616;
    --matte-soft: #2c2c2c;
    --white: #ffffff;
    --ink: #111111;
    --shade: #a8a8a8;
    --rule: #222222;
    --muted: #6f6f6f;
  }
  * { margin: 0; padding: 0; box-sizing: border-box; }
  html, body {
    width: 1200px;
    height: 693px;
    overflow: hidden;
    background: var(--white);
  }
  .card {
    position: relative;
    width: 1200px;
    height: 693px;
    background: var(--white);
    font-family: "Josefin Slab", Georgia, serif;
    color: var(--ink);
  }
  .header-band {
    position: absolute;
    left: 0; top: 0;
    width: 1200px;
    height: 246px;
    background: var(--matte);
  }
  .header-rule {
    position: absolute;
    left: 0; top: 249px;
    width: 1200px;
    height: 2px;
    background: var(--matte);
  }
  .brand-name {
    position: absolute;
    left: 68px;
    top: 98px;
    font-weight: 700;
    font-size: 54px;
    line-height: 1;
    color: var(--white);
  }
  .tagline {
    position: absolute;
    left: 96px;
    top: 166px;
    font-weight: 400;
    font-size: 38px;
    line-height: 1;
    color: var(--white);
  }
  .map-decoration {
    position: absolute;
    left: 943px;
    top: 45px;
    width: 204px;
    height: 170px;
    border-radius: 40px;
    background: radial-gradient(ellipse at center, var(--matte-soft) 0%, var(--matte) 75%);
  }
  .divider {
    position: absolute;
    left: 512px;
    top: 373px;
    width: 2px;
    height: 194px;
    background: var(--rule);
  }
  .person-name {
    position: absolute;
    left: 70px;
    top: 418px;
    font-family: "Yellowtail", cursive;
    font-size: 70px;
    line-height: 1;
    white-space: nowrap;
    color: var(--ink);
    text-shadow: 4px 3px 0 var(--shade);
  }
  .licence {
    position: absolute;
    left: 269px;
    top: 487px;
    font-size: 16px;
    letter-spacing: 1px;
    line-height: 1;
    color: var(--ink);
  }
  .contact {
    position: absolute;
    right: 71px;
    top: 474px;
    text-align: right;
    font-size: 36px;
    line-height: 44px;
    white-space: nowrap;
    color: var(--ink);
  }
  .contact .accent { color: var(--muted); }
</style>
</head>
<body>
  <div class="card">
    <div class="header-band"></div>
    <div class="header-rule"></div>

    <div class="brand-name">Summit Check &amp; Label</div>
    <div class="tagline">Onsite Electrical Testing &amp; Tagging</div>
    <div class="map-decoration" role="img" aria-label="Faint map of Australia decoration"></div>

    <div class="person-name">Greg Palmby</div>
    <div class="licence">Licence No. 48213</div>

    <div class="divider"></div>

    <div class="contact">
      <div class="phone">0417.592.348</div>
      <div class="email">greg@summit<span class="accent">check</span>and<span class="accent">label</span>.com.au</div>
    </div>
  </div>
</body>
</html>
```